Web Design - Website with Group Buying

We are a startup company based in Boston, MA looking for a professional individual or team to redesign our web page. The website has a unique approach to it. It is an eCommerce website, however it focuses on a mixed concept of crowd buying and tiered pricing.

We intend to bring a fun social atmosphere to buying products/services/goods online. As a result of the social concept, consumers will be able to buy items together resulting in a “bulk” purchase from a merchant perspective.

What does this allow? Simple. Higher quantities allow merchants to drive down pricing per unit resulting in a deal for everyone.

We have a beta, and a design, however the CEO is looking to see if someone can make the concept more visually appealing, and comprehensive. We need someone who is creative in portraying the idea better, so our consumers can easily understand what is going on. We heavily rely on the design of this page. We are open to colors, and schemes, but do like some of the modern eCommerce platforms today, such as www.brisvale.com.

Attached you will find the original mock up of the idea. Keep in mind we have gone through iterations, but the CEO feels this standard mockup displays how the ecommerce platform works.

WHAT IS NEEDED?
Must have a minimum of two pages. The home page, and what we call the Deal Details Page. The focus is heavily on the deal details page. We are in need for someone to creatively come up with a new approach to the design. DO NOT COPY the design as is, please try to give your own perspective as you deem fit.

Industry/Entity Type

Retail

Number of Pages Required

2 page

Requirements
Must have
• Must have two pages. The home page, and what we call the Deal Details Page. The focus is heavily on the deal details page. We are in need for someone to creatively come up with a new approach to the design. DO NOT COPY the design as is, please try to give your own perspective as you deem fit.
Nice to have
• Creative thinking.
• We are in need for someone to creatively come up with a new approach to the design. DO NOT COPY the design as is, please try to give your own perspective as you deem fit.
Should not have
• DO NOT COPY the design as is, please try to give your own perspective as you deem fit.

```html
<!DOCTYPE html>
<html lang="en">
<head>
<meta charset="utf-8">
<title>Groupwell – Deal Details</title>
<link href="https://fonts.googleapis.com/css2?family=Raleway:wght@400;500&family=Open+Sans:wght@400;600&family=Exo+2:wght@400&display=swap" rel="stylesheet">
<style>
:root{
  --blue:#0a7fd2;
  --blue-dark:#0758ad;
  --blue-text:#1a8ad4;
  --orange:#f57f0a;
  --orange-light:#fb9a1c;
  --ink:#333;
  --muted:#666;
  --line:#c9c9c9;
  --panel:#ececec;
  --footer:#262626;
}
*{margin:0;padding:0;box-sizing:border-box}
html,body{width:1200px;height:1093px;overflow:hidden;background:#fff}
.page{position:absolute;left:0;top:0;width:1366px;height:1244px;transform:scale(.87848);transform-origin:0 0;font-family:"Open Sans",sans-serif;color:var(--ink);font-variant-numeric:lining-nums;font-feature-settings:"lnum" 1}
.abs{position:absolute}
.site-header{left:0;top:0;width:1366px;height:111px;background:linear-gradient(#0a86d8,var(--blue-dark))}
.brand{left:212px;top:36px;font:400 31px "Raleway",sans-serif;color:#fff}
.search{left:434px;top:39px;width:376px;height:37px;border-radius:19px;background:#fff;border:2px solid #cfe3f3}
.search span{position:absolute;left:20px;top:8px;font-size:14px;color:#999}
.search-btn{position:absolute;right:3px;top:2px;width:30px;height:30px;border-radius:50%;background:var(--blue)}
.nav-item{top:0;height:111px;text-align:center;color:#fff;font:400 16px "Raleway",sans-serif;padding-top:24px}
.nav-item svg{display:block;margin:0 auto 6px}
.nav-sep{top:0;width:1px;height:111px;background:rgba(255,255,255,.2)}
.photo{border:1px solid var(--line)}
.photo-fill{width:100%;height:100%;background:linear-gradient(135deg,#f4f4f4,#d9dcdf 60%,#eef0f2)}
.notes-title{left:212px;top:566px;font-size:16px;color:var(--blue-text)}
.note{left:212px;width:545px;font-size:11.6px;line-height:15px;padding-left:22px;color:#333}
.note svg{position:absolute;left:0;top:1px}
.deal-panel{left:762px;top:139px;width:393px;height:610px;border:1px solid var(--line)}
.tier-area{left:0;top:0;width:391px;height:283px;background:linear-gradient(#e6e6e6,#f3f3f3)}
.price-now{left:0;top:22px;width:100%;text-align:center;font:400 22px "Raleway",sans-serif;color:var(--blue-text)}
.price-retail{left:0;top:57px;width:100%;text-align:center;font-size:17px}
.tier{width:90px;height:90px;border-radius:50%;border:5px solid #ddd;display:flex;align-items:center;justify-content:center;font:400 21px "Raleway",sans-serif;font-variant-numeric:lining-nums}
.tier-label{width:90px;text-align:center;font-size:13px;line-height:16px;color:#444}
.blurb{left:30px;top:310px;width:333px;text-align:center;font-size:11px;line-height:20.5px;color:#777}
.qty-label{left:43px;top:394px;font-size:15px}
.qty{left:85px;top:388px;width:92px;height:34px;border:1px solid #ccc;font-size:13px;padding:8px 10px;color:#444}
.cta{left:202px;top:389px;width:134px;height:32px;background:linear-gradient(var(--orange-light),var(--orange));color:#fff;font:400 15px "Raleway",sans-serif;text-align:center;line-height:32px}
.share{top:436px;width:31px;height:31px;border-radius:50%}
.count{top:490px;width:58px;height:67px;background:linear-gradient(#1296e2,var(--blue-dark));color:#fff;font:400 36px "Exo 2",sans-serif;text-align:center;line-height:67px}
.count-label{top:564px;width:70px;text-align:center;font-size:11px;color:#444}
.tab{top:824px;height:45px;border:1px solid var(--line);border-bottom:none;font:500 15px "Raleway",sans-serif;text-align:center;line-height:45px;color:#333}
.tab.active{background:#999;color:#fff;border-color:#999}
.tab-body{left:206px;top:869px;width:954px;height:251px;border:1px solid var(--line);padding:32px 24px 0 34px;font-size:13px;line-height:20.4px;color:#555}
.tab-body p+p{margin-top:24px;padding-left:4px}
.site-footer{left:0;top:1182px;width:1366px;height:62px;background:var(--footer);color:#bbb;font-size:14px;padding:24px 0 0 210px}
</style>
</head>
<body>
<div class="page">
  <header class="abs site-header">
    <div class="abs brand">Groupwell</div>
    <div class="abs search"><span>Search here</span>
      <div class="search-btn"><svg width="30" height="30" viewBox="0 0 30 30"><circle cx="14" cy="14" r="5" fill="none" stroke="#fff" stroke-width="2"/><line x1="17.5" y1="17.5" x2="20.5" y2="20.5" stroke="#fff" stroke-width="2.2" stroke-linecap="round"/></svg></div>
    </div>
    <div class="abs nav-item" style="left:872px;width:84px">
      <svg width="18" height="20" viewBox="0 0 18 20"><path d="M5 9V6a4 4 0 0 1 8 0v3" fill="none" stroke="#fff" stroke-width="2"/><rect x="2" y="9" width="14" height="11" rx="1.5" fill="#fff"/></svg>LOGIN</div>
    <div class="abs nav-sep" style="left:956px"></div>
    <div class="abs nav-item" style="left:957px;width:111px">
      <svg width="20" height="20" viewBox="0 0 20 20"><circle cx="10" cy="5.5" r="5" fill="#fff"/><path d="M1 20a9 8 0 0 1 18 0z" fill="#fff"/></svg>REGISTER</div>
    <div class="abs nav-sep" style="left:1068px"></div>
    <div class="abs nav-item" style="left:1069px;width:82px">
      <svg width="24" height="20" viewBox="0 0 24 20"><path d="M1 2h4l3 11h12l2-8H7" fill="none" stroke="#fff" stroke-width="2"/><circle cx="9" cy="17" r="2" fill="#fff"/><circle cx="18" cy="17" r="2" fill="#fff"/></svg>CART</div>
  </header>

  <div class="abs photo" style="left:206px;top:139px;width:546px;height:319px"><div class="photo-fill" role="img" aria-label="Product photo: white tablet shown front and back"></div></div>
  <div class="abs photo" style="left:206px;top:473px;width:131px;height:80px"><div class="photo-fill" role="img" aria-label="Thumbnail: pair of speakers"></div></div>
  <div class="abs photo" style="left:343px;top:473px;width:131px;height:80px"><div class="photo-fill" role="img" aria-label="Thumbnail: compact camera"></div></div>
  <div class="abs photo" style="left:483px;top:473px;width:131px;height:80px"><div class="photo-fill" role="img" aria-label="Thumbnail: smartphone"></div></div>
  <div class="abs photo" style="left:620px;top:473px;width:131px;height:80px"><div class="photo-fill" role="img" aria-label="Thumbnail: video camcorder"></div></div>

  <h2 class="abs notes-title" style="font-weight:400">KEY NOTES</h2>
  <div class="abs note" style="top:602px"><svg width="16" height="16" viewBox="0 0 16 16"><circle cx="8" cy="8" r="8" fill="var(--blue-text)"/><path d="M4.5 8.2l2.3 2.3 4.5-4.6" fill="none" stroke="#fff" stroke-width="2"/></svg>The deal is only VALID if the first tier is reached. An automatic trigger will happen when 1000<br>have joined the deal indicating that the deal is ON/valid</div>
  <div class="abs note" style="top:649px"><svg width="16" height="16" viewBox="0 0 16 16"><circle cx="8" cy="8" r="8" fill="var(--blue-text)"/><path d="M4.5 8.2l2.3 2.3 4.5-4.6" fill="none" stroke="#fff" stroke-width="2"/></svg>After the first tier is reached, the customer will have the option to either Join the deal currently<br>, or Only join the deal if the second tier is reached.</div>
  <div class="abs note" style="top:696px"><svg width="16" height="16" viewBox="0 0 16 16"><circle cx="8" cy="8" r="8" fill="var(--blue-text)"/><path d="M4.5 8.2l2.3 2.3 4.5-4.6" fill="none" stroke="#fff" stroke-width="2"/></svg>After the second tier is reached, the customer will have the option either join the deal<br>currently, or Only Join the deal if the third tier is reached.</div>
  <div class="abs note" style="top:743px"><svg width="16" height="16" viewBox="0 0 16 16"><circle cx="8" cy="8" r="8" fill="var(--blue-text)"/><path d="M4.5 8.2l2.3 2.3 4.5-4.6" fill="none" stroke="#fff" stroke-width="2"/></svg>ALL BUYERS WILL RECEIVE THE LOWEST TIER REACHED</div>

  <section class="abs deal-panel">
    <div class="abs tier-area">
      <div class="abs price-now">Current Prices: $100.00</div>
      <div class="abs price-retail">Retial Value: $150</div>
      <svg class="abs" style="left:0;top:190px" width="391" height="20"><line x1="70" y1="10" x2="322" y2="10" stroke="#aaa" stroke-width="3"/><circle cx="70" cy="10" r="7" fill="#ddd"/><circle cx="193" cy="10" r="7" fill="#777"/><circle cx="322" cy="10" r="7" fill="var(--blue)"/></svg>
      <div class="abs tier" style="left:32px;top:98px;background:#eee;color:#777">$150</div>
      <div class="abs tier" style="left:148px;top:98px;background:#777;color:#fff">$100</div>
      <div class="abs tier" style="left:276px;top:98px;background:var(--blue);color:#fff">$70</div>
      <div class="abs tier-label" style="left:28px;top:212px">100<br>Peoples</div>
      <div class="abs tier-label" style="left:148px;top:212px">500<br>Peoples</div>
      <div class="abs tier-label" style="left:279px;top:212px">1000<br>Peoples</div>
    </div>
    <p class="abs blurb">Ut nisi erat fermentum vel congue id euismod in elit Fusce ultricies orci ac feugiat suscipit leo massa sodales velit et scelerisque mi tortor at ipsum cligula augue</p>
    <div class="abs qty-label">QTY:</div>
    <div class="abs qty">01<svg style="position:absolute;right:8px;top:7px" width="10" height="18" viewBox="0 0 10 18"><path d="M1 6l4-4 4 4M1 12l4 4 4-4" fill="none" stroke="#666" stroke-width="1.4"/></svg></div>
    <div class="abs cta">JOIN THE DEAL</div>
    <div class="abs share" style="left:39px;background:#5bb3e6" role="img" aria-label="Share"></div>
    <div class="abs share" style="left:76px;background:#2f5a9e" role="img" aria-label="Share"></div>
    <div class="abs share" style="left:113px;background:#0b6f93" role="img" aria-label="Share"></div>
    <div class="abs share" style="left:149px;background:#d9422f" role="img" aria-label="Share"></div>
    <div class="abs count" style="left:42px">08</div>
    <div class="abs count" style="left:113px">23</div>
    <div class="abs count" style="left:183px">25</div>
    <div class="abs count" style="left:253px">12</div>
    <div class="abs count-label" style="left:36px">DAYS</div>
    <div class="abs count-label" style="left:106px">HOURS</div>
    <div class="abs count-label" style="left:179px">MINUTES</div>
    <div class="abs count-label" style="left:247px">SECOND</div>
  </section>

  <div class="abs tab active" style="left:206px;width:204px">OVERVIEW</div>
  <div class="abs tab" style="left:410px;width:204px">SPECIFICATION</div>
  <div class="abs tab" style="left:613px;width:205px">SHOPPING &amp; RETURNS</div>
  <div class="abs tab-body">
    <p>When the deal is live, the system will clearly communicate the retail value of the hat, and that the deal isnot ON/valid until 100 products are sold. Now when 100 products are sold, there will be an indicator that shows the deal is ON/VALID. As more people join, the “Current Price” of the product will display of the last tier. So if 101 people join, the current price will show 150. If, let’ say at the end of the deal there will be 650 people decide to join the deal. All 650 people will now receive the price of the hat for $100.00.</p>
    <p>In addition, the system must show the number of units needed to be sold to reach the next tier. Need to encourage user to reach goal.</p>
  </div>

  <footer class="abs site-footer">© 2015 Company Name &nbsp;All right reserved &nbsp;Term of Use</footer>
</div>
</body>
</html>
```